Awesome Pavement Maintenance Company Needs New Postcard!

We are an Asphalt Maintenance contractor in need of a new Postcard design for our Fall direct mail campaign. Our services include Crack Filling, Sealcoating, Line Striping and Asphalt Patching. Fall is a busy time of year for Parking Lot Maintenance services in Connecticut, USA where we are located, and we need to capture as much business from this mail piece as we possibly can. People enlist our services in preparation for winter so the winning design will have a call to action that we think has the best chance of getting our phone to ring. Come up with a new look and feel for us in your design.

Feel free to use our images attached, or stock images. An example of one of our current cards is attached also. PLEASE: use the template provided for layout specifications.

Target Market(s)

Commercial/Industrial Facility Managers, Condo/Apartment Building Property Managers, Owners of Commercial Real Estate, Business Owners, etc.

Industry/Entity Type

Construction Company

Requirements
Must have
• A Call to Action
• Our Phone Number: 860-417-2938
• Our website: www.brinweldpavement.example
Nice to have
• Our 4 Main Services Listed
• -Asphalt Patching
• - Crack Filling
• -Sealcoating
• -Line Striping
• Photos? We have plenty or use stock
Should not have
• Misspelling of our name. Should be BrinWELD -not 'coast'!

```html
<!DOCTYPE html>
<html lang="en">
<head>
<meta charset="utf-8">
<title>BrinWELD Pavement Services – Fall Postcard</title>
<link rel="stylesheet" href="https://fonts.googleapis.com/css2?family=Oswald:wght@600;700&family=Roboto+Condensed:wght@400;700&family=PT+Serif:ital,wght@0,400;0,700;1,700&display=swap">
<style>
  :root{
    --red:#d7141b;
    --black:#141414;
    --white:#ffffff;
    --page:#e9e9e9;
    --yellow:#f5b915;
    --ink:#1d1d1d;
    --stamp:#3a3a3a;
    --grass:#6f8a4a;
    --asphalt:#5d6268;
  }
  *{box-sizing:border-box;margin:0;padding:0}
  html,body{width:907px;height:1200px;overflow:hidden}
  body{background:var(--page);position:relative;font-family:"Roboto Condensed",Arial,sans-serif;color:var(--ink)}
  .card{position:absolute;left:92px;width:736px;height:460px;background:var(--white);overflow:hidden;box-shadow:0 2px 6px rgba(0,0,0,.18)}
  .card--front{top:52px}
  .card--back{top:624px}
  .card__art{position:absolute;inset:0;width:736px;height:460px}
  .brand{position:absolute;text-align:center}
  .brand__name{display:block;font-family:"Oswald",Arial,sans-serif;font-weight:700;font-size:38px;line-height:1;color:var(--red);letter-spacing:.5px}
  .brand__tag{display:block;font-family:"Roboto Condensed",Arial,sans-serif;font-weight:700;font-size:14px;letter-spacing:1px;color:var(--black);margin-top:4px}
  .front .brand{left:44px;top:16px;width:210px}
  .headline{position:absolute;left:28px;top:86px;width:290px;text-align:center}
  .headline__ask{font-family:"Oswald",Arial,sans-serif;font-weight:700;font-size:37px;line-height:1;color:var(--red)}
  .headline__season{font-family:"PT Serif",Georgia,serif;font-weight:700;font-size:31px;line-height:1.1;color:var(--black)}
  .services{position:absolute;left:22px;top:190px;width:300px;display:grid;grid-template-columns:146px 150px;row-gap:11px;list-style:none;font-size:17px}
  .services li{display:flex;align-items:center;gap:6px}
  .tick{width:12px;height:12px;flex:none}
  .testimonial{position:absolute;left:12px;top:262px;width:320px;font-size:10.6px;line-height:1.3}
  .testimonial__mark{position:absolute;font-family:"PT Serif",Georgia,serif;font-weight:700;font-size:34px;color:var(--red);line-height:1}
  .testimonial__mark--open{left:0;top:-6px}
  .testimonial__mark--close{left:190px;top:30px}
  .testimonial__text{padding-left:26px}
  .testimonial__by{margin-left:220px;margin-top:6px;line-height:1.1}
  .testimonial__name{font-family:"PT Serif",Georgia,serif;font-size:16px;color:var(--red)}
  .testimonial__org{font-style:italic;font-size:10px}
  .offer{position:absolute;left:369px;top:244px;width:144px;height:144px;border-radius:50%;text-align:center;padding-top:22px}
  .offer__free{font-family:"Oswald",Arial,sans-serif;font-weight:700;font-size:40px;line-height:1;color:var(--red)}
  .offer__what{font-family:"PT Serif",Georgia,serif;font-size:18px;line-height:1.1;color:var(--black)}
  .offer__fast{font-family:"PT Serif",Georgia,serif;font-weight:700;font-style:italic;font-size:30px;line-height:1;color:var(--red)}
  .contact-bar{position:absolute;left:14px;top:416px;display:flex;align-items:center;gap:16px;color:var(--white)}
  .contact-bar__phone{font-family:"Roboto Condensed",Arial,sans-serif;font-weight:700;font-size:22px;display:flex;align-items:center;gap:6px}
  .contact-bar__web{font-size:15px;display:flex;align-items:center;gap:5px}
  .icon{width:16px;height:16px;flex:none}
  .back .brand{left:14px;top:20px;width:200px}
  .back .brand__name{font-size:34px}
  .address{position:absolute;left:232px;top:26px;font-size:14px;line-height:1.25;font-style:normal}
  .address__web{color:var(--red)}
  .about{position:absolute;left:18px;top:100px;width:370px}
  .about__title{text-align:center;font-family:"Oswald",Arial,sans-serif;font-weight:700;font-size:44px;line-height:1;color:var(--red)}
  .about__sub{text-align:center;font-family:"PT Serif",Georgia,serif;font-size:26px;line-height:1.1;color:var(--black)}
  .about__text{margin-top:10px;font-size:10.8px;line-height:1.3;width:330px}
  .call{position:absolute;left:16px;top:346px;color:var(--white)}
  .call__avail{font-family:"PT Serif",Georgia,serif;font-size:8px;color:var(--yellow);letter-spacing:.3px}
  .call__answer{font-weight:700;font-size:12px}
  .call__ask{font-family:"Oswald",Arial,sans-serif;font-weight:700;font-size:19px;color:var(--red);margin-top:8px;line-height:1}
  .call__phone{font-weight:700;font-size:30px;line-height:1.1}
  .stamp{position:absolute;left:612px;top:18px;width:80px;height:100px;background:var(--stamp)}
</style>
</head>
<body>

<section class="card card--front front">
  <svg class="card__art" viewBox="0 0 736 460">
    <defs>
      <linearGradient id="siteFront" x1="0" y1="0" x2="0.4" y2="1">
        <stop offset="0" stop-color="#7d9558"/>
        <stop offset="0.45" stop-color="var(--grass)"/>
        <stop offset="0.7" stop-color="#7a8088"/>
        <stop offset="1" stop-color="var(--asphalt)"/>
      </linearGradient>
      <linearGradient id="frost" x1="0" y1="0" x2="0" y2="1">
        <stop offset="0" stop-color="#ffffff"/>
        <stop offset="1" stop-color="#e4e6e8"/>
      </linearGradient>
    </defs>
    <rect width="736" height="460" fill="url(#frost)"/>
    <path role="img" aria-label="Aerial photo of an office building and freshly sealed parking lot, with a worker line striping a lot" d="M330,0 H736 V460 H470 C410,380 350,260 338,150 C333,100 330,50 330,0 Z" fill="url(#siteFront)"/>
    <path d="M330,0 C330,50 333,100 338,150 C350,260 410,380 470,460" fill="none" stroke="var(--red)" stroke-width="14"/>
    <path d="M0,372 C140,410 330,400 440,318 L480,460 H0 Z" fill="var(--black)"/>
    <path d="M0,372 C140,410 330,400 440,318" fill="none" stroke="var(--red)" stroke-width="8"/>
    <path d="M500,290 C560,258 620,240 680,232" fill="none" stroke="var(--red)" stroke-width="20"/>
    <path d="M672,202 L712,228 L680,264 Z" fill="var(--red)"/>
    <circle cx="441" cy="316" r="76" fill="var(--red)"/>
    <circle cx="441" cy="316" r="70" fill="var(--yellow)"/>
  </svg>

  <div class="brand">
    <span class="brand__name">BrinWELD</span>
    <span class="brand__tag">PAVEMENT SERVICES</span>
  </div>

  <div class="headline">
    <div class="headline__ask">ARE YOU READY</div>
    <div class="headline__season">FOR WINTER?</div>
  </div>

  <ul class="services">
    <li><svg class="tick" viewBox="0 0 12 12"><circle cx="6" cy="6" r="6" fill="var(--red)"/><path d="M3.2,6.2 L5.2,8 L8.8,4" fill="none" stroke="#fff" stroke-width="1.6"/></svg>Sealcoating</li>
    <li><svg class="tick" viewBox="0 0 12 12"><circle cx="6" cy="6" r="6" fill="var(--red)"/><path d="M3.2,6.2 L5.2,8 L8.8,4" fill="none" stroke="#fff" stroke-width="1.6"/></svg>Crack Filling</li>
    <li><svg class="tick" viewBox="0 0 12 12"><circle cx="6" cy="6" r="6" fill="var(--red)"/><path d="M3.2,6.2 L5.2,8 L8.8,4" fill="none" stroke="#fff" stroke-width="1.6"/></svg>Line Striping</li>
    <li><svg class="tick" viewBox="0 0 12 12"><circle cx="6" cy="6" r="6" fill="var(--red)"/><path d="M3.2,6.2 L5.2,8 L8.8,4" fill="none" stroke="#fff" stroke-width="1.6"/></svg>Paving &amp; Repair</li>
  </ul>

  <blockquote class="testimonial">
    <span class="testimonial__mark testimonial__mark--open">&ldquo;</span>
    <p class="testimonial__text">BrinWELD Pavement Services were true professionals that worked to accommodate our employee's schedule and our parking lots have not looked this good in years</p>
    <span class="testimonial__mark testimonial__mark--close">&rdquo;</span>
    <footer class="testimonial__by">
      <div class="testimonial__name">Dale Hurvick</div>
      <div class="testimonial__org">norvane tool works<br>A publicly listed company</div>
    </footer>
  </blockquote>

  <div class="offer">
    <div class="offer__free">FREE</div>
    <div class="offer__what">ESTIMATES</div>
    <div class="offer__fast">Fast!</div>
  </div>

  <div class="contact-bar">
    <span class="contact-bar__phone"><svg class="icon" viewBox="0 0 16 16"><rect width="16" height="16" rx="3" fill="var(--yellow)"/><path d="M5,3 L7,5 L6,7 C7,9 8,10 9.5,10.5 L11,9.5 L13,11.5 L11.5,13 C7,12.5 3.5,9 3.2,4.6 Z" fill="var(--black)"/></svg>860.417.2938</span>
    <span class="contact-bar__web"><svg class="icon" viewBox="0 0 16 16"><circle cx="8" cy="8" r="7" fill="none" stroke="var(--yellow)" stroke-width="1.5"/><path d="M1,8 H15 M8,1 C4,5 4,11 8,15 M8,1 C12,5 12,11 8,15" fill="none" stroke="var(--yellow)" stroke-width="1.2"/></svg>brinweldpavement.example</span>
  </div>
</section>

<section class="card card--back back">
  <svg class="card__art" viewBox="0 0 736 460">
    <defs>
      <linearGradient id="frostBack" x1="0" y1="0" x2="0" y2="1">
        <stop offset="0" stop-color="#ffffff"/>
        <stop offset="1" stop-color="#e2e4e6"/>
      </linearGradient>
      <linearGradient id="siteBack" x1="0" y1="0" x2="0" y2="1">
        <stop offset="0" stop-color="#8a9d6a"/>
        <stop offset="0.5" stop-color="var(--asphalt)"/>
        <stop offset="1" stop-color="#748a55"/>
      </linearGradient>
    </defs>
    <rect width="736" height="460" fill="#fff"/>
    <path d="M0,0 H392 C420,90 405,190 330,300 L0,300 Z" fill="url(#frostBack)"/>
    <path d="M392,0 C420,90 405,190 330,300" fill="none" stroke="var(--red)" stroke-width="10"/>
    <path d="M0,320 C80,318 160,310 230,300 C260,360 300,420 330,460 H0 Z" fill="var(--black)"/>
    <path d="M200,272 C140,282 80,286 40,286" fill="none" stroke="var(--red)" stroke-width="18"/>
    <path d="M44,258 L4,286 L44,312 Z" fill="var(--red)"/>
    <circle cx="270" cy="350" r="66" fill="var(--red)"/>
    <circle role="img" aria-label="Aerial photo of a large sealcoated and striped parking lot" cx="270" cy="350" r="58" fill="url(#siteBack)"/>
  </svg>

  <div class="brand">
    <span class="brand__name">BrinWELD</span>
    <span class="brand__tag">PAVEMENT SERVICES</span>
  </div>

  <address class="address">
    P.O. Box 382<br>
    Ashford Bay, CT 06115<br>
    <span class="address__web">brinweldpavement.example</span>
  </address>

  <div class="about">
    <div class="about__title">BRINWELD</div>
    <div class="about__sub">PAVEMENT SERVICES</div>
    <p class="about__text">is a reliable, service-oriented group of professionals working for those that expect the best. We strive to provide our customers with the highest level of pavement maintenance expertise, superior quality and unsurpassed service.</p>
  </div>

  <div class="call">
    <div class="call__avail">BRINWELD EXPERTS ARE AVAILABLE</div>
    <div class="call__answer">TO ANSWER YOUR REQUESTS</div>
    <div class="call__ask">PLEASE CALL US AT</div>
    <div class="call__phone">860.417.2938</div>
  </div>

  <div class="stamp"></div>
</section>

</body>
</html>
```